Lotus Market Hall VIP Card(Magnetic strip plastic card)

We need Fancy,Simple,VIP customer card design for a grocery store name"Lotus Market Hall", Chinese name"鸿福商场“.Major color should be Dark red. This design is based on a VIP gift card project, which means design should consider about the back side with magnetic strip area and mostly it will be plastic material.

Target Market(s)

Rich Customers

Industry/Entity Type

Grocery Store

Contact Information for Business Card

People actually put more than $1000 into the card for shopping

Font styles to use
Serif
Sans Serif
Decorative
Script
Other font styles liked:
• Fancy

Colors
ec1f27
fbed22

Requirements
Must have
• Red color
Nice to have
• Better logo transformation.

```html
<!DOCTYPE html>
<html lang="en">
<head>
<meta charset="utf-8">
<title>Lotus Market Hall – VIP Card Design</title>
<link rel="stylesheet" href="https://fonts.googleapis.com/css2?family=Alegreya:wght@400;500&family=Noto+Serif+SC:wght@600&display=swap">
<style>
  :root {
    --backdrop: #d9d2c8;
    --card-red-deep: #5e0a10;
    --card-red: #8c121b;
    --accent-gold: #f3d35a;
    --text-light: #f6efe6;
    --seal-tone: #d8cfbd;
    --strip: #111111;
    --shadow: rgba(40, 25, 10, 0.35);
  }
  * { margin: 0; padding: 0; box-sizing: border-box; }
  html, body {
    width: 1200px;
    height: 900px;
    overflow: hidden;
    background: var(--backdrop);
    font-family: "Alegreya", Georgia, serif;
  }
  .canvas { position: relative; width: 1200px; height: 900px; }

  .card {
    position: absolute;
    width: 580px;
    height: 330px;
    background: linear-gradient(135deg, var(--card-red) 0%, var(--card-red-deep) 100%);
    border-radius: 14px;
    box-shadow: 0 14px 30px var(--shadow);
    color: var(--text-light);
    overflow: hidden;
  }
  .card--front { left: 70px; top: 80px; }
  .card--back  { left: 550px; top: 490px; }

  .magnetic-strip {
    position: absolute;
    left: 0;
    right: 0;
    top: 26px;
    height: 52px;
    background: var(--strip);
  }

  .brand {
    position: absolute;
    display: flex;
    align-items: center;
    gap: 14px;
  }
  .brand__seal {
    border-radius: 50%;
    background: var(--seal-tone);
    flex: none;
  }
  .brand__names { display: flex; flex-direction: column; line-height: 1.05; }
  .brand__cn {
    font-family: "Noto Serif SC", "Alegreya", serif;
    font-weight: 600;
    color: var(--accent-gold);
  }
  .brand__en { color: var(--text-light); font-weight: 400; }

  .card--front .brand { left: 50%; top: 50%; transform: translate(-50%, -50%); }
  .card--front .brand__seal { width: 96px; height: 96px; }
  .card--front .brand__cn { font-size: 40px; letter-spacing: 2px; }
  .card--front .brand__en { font-size: 17px; margin-top: 4px; }

  .card--back .brand { right: 28px; top: 94px; gap: 10px; }
  .card--back .brand__seal { width: 62px; height: 62px; }
  .card--back .brand__cn { font-size: 26px; letter-spacing: 1px; }
  .card--back .brand__en { font-size: 13px; margin-top: 3px; }

  .holder { position: absolute; left: 40px; top: 150px; }
  .holder__name { color: var(--accent-gold); font-size: 26px; font-weight: 400; }
  .holder__role { font-size: 16px; margin-top: 2px; }

  .contact {
    position: absolute;
    left: 40px;
    top: 232px;
    font-size: 15px;
    line-height: 1.45;
  }
  .contact__label { color: var(--accent-gold); }
  .contact__web { color: var(--accent-gold); }
  .contact__gap { display: inline-block; width: 10px; }
</style>
</head>
<body>
<main class="canvas">

  <section class="card card--front" aria-label="Card front">
    <div class="brand">
      <span class="brand__seal" aria-hidden="true"></span>
      <div class="brand__names">
        <span class="brand__cn">鸿福商场</span>
        <span class="brand__en">Lotus Market Hall</span>
      </div>
    </div>
  </section>

  <section class="card card--back" aria-label="Card back">
    <div class="magnetic-strip" aria-hidden="true"></div>

    <div class="brand">
      <span class="brand__seal" aria-hidden="true"></span>
      <div class="brand__names">
        <span class="brand__cn">鸿福商场</span>
        <span class="brand__en">Lotus Market Hall</span>
      </div>
    </div>

    <div class="holder">
      <p class="holder__name">Daniel Harper</p>
      <p class="holder__role">Managing Director</p>
    </div>

    <div class="contact">
      <p>1234, Address GoesHere, Country, 12345</p>
      <p>
        <span class="contact__label">T:</span> (044) 123 456 789<span class="contact__gap"></span>
        <span class="contact__label">F:</span> (044) 123456789<span class="contact__gap"></span>
        <span class="contact__label">M:</span> (044)123456789
      </p>
      <p>
        <span class="contact__label">E:</span> info@youremail.com<span class="contact__gap"></span>
        <span class="contact__web">www.yourweb.com</span>
      </p>
    </div>
  </section>

</main>
</body>
</html>
```